New Architectural Firm Business Cards

New Business card to compliment previous pixel forum logo (attached). Please design a business card that is simple, modern, creative....please do not use "symbols", simply the logo and associated graphics/text. The front should contain name/address/phone/email/web address (with graphics).....back should be 100% graphic design using the logo somehow. Hoping for a two color (black and yellow) design. full bleed design, no borders

Target Market(s)

Commercial Architecture Clients

Industry/Entity Type

Architecture

Contact Information for Business Card

Please design a business card that is simple, modern, creative....please do not use "symbols", simply the logo and associated graphics/text. The front should contain name/address/phone/email/web address (with graphics).....back should be 100% graphic design using the logo somehow

Font styles to use
Sans Serif

Colors
FFF300
FFF600
FEFA6F
FFFEC7
FFFEE8

Requirements
Must have
• Clean, Modern Design
Should not have
• Stock images or "icons"

```html
<!DOCTYPE html>
<html lang="en">
<head>
<meta charset="utf-8">
<title>Pixel Forum Architecture – Business Cards</title>
<link rel="stylesheet" href="https://fonts.googleapis.com/css2?family=Montserrat:wght@500;700;800&display=swap">
<style>
  :root {
    --page: #ffffff;
    --ink: #111111;
    --yellow: #f6c21c;
    --yellow-deep: #e0ab0f;
    --card-shadow: rgba(0, 0, 0, 0.28);
  }
  * { margin: 0; padding: 0; box-sizing: border-box; }
  html, body {
    width: 1200px;
    height: 1079px;
    overflow: hidden;
    background: var(--page);
    font-family: "Montserrat", Arial, sans-serif;
  }
  .sheet {
    position: relative;
    width: 1200px;
    height: 1079px;
  }
  .card {
    position: absolute;
    top: 381px;
    width: 540px;
    height: 316px;
    overflow: hidden;
    box-shadow: 6px 6px 10px var(--card-shadow);
  }
  /* Back side */
  .card-back {
    left: 40px;
    background: var(--ink);
  }
  .card-back .artwork {
    position: absolute;
    left: 0;
    top: 0;
    width: 100%;
    height: 100%;
    background:
      radial-gradient(ellipse 45% 70% at 22% 45%, rgba(246, 194, 28, 0.42), rgba(246, 194, 28, 0.08) 70%, transparent 100%),
      linear-gradient(90deg, rgba(255, 255, 255, 0.05), rgba(255, 255, 255, 0.02));
  }
  .back-brand {
    position: absolute;
    left: 340px;
    top: 84px;
    color: var(--yellow);
    font-weight: 800;
    line-height: 1;
  }
  .back-brand .brand-name {
    display: block;
    font-size: 46px;
    letter-spacing: -1px;
  }
  .back-brand .brand-tag {
    display: block;
    margin-top: 8px;
    font-size: 20px;
    font-weight: 700;
    letter-spacing: 0.2px;
  }
  /* Front side */
  .card-front {
    left: 620px;
    background: var(--yellow);
    color: var(--ink);
  }
  .front-brand {
    position: absolute;
    right: 40px;
    top: 44px;
    text-align: center;
    line-height: 1;
  }
  .front-brand .brand-name {
    display: block;
    font-size: 30px;
    font-weight: 800;
    letter-spacing: -0.5px;
  }
  .front-brand .brand-tag {
    display: block;
    margin-top: 4px;
    font-size: 10px;
    font-weight: 700;
  }
  .role-line {
    position: absolute;
    right: 30px;
    top: 166px;
    font-size: 20px;
    font-weight: 500;
    letter-spacing: 0.2px;
  }
  .role-line .person { font-weight: 800; }
  .divider {
    position: absolute;
    right: 0;
    top: 196px;
    width: 270px;
    height: 1.5px;
    background: var(--ink);
  }
  .contact-list {
    position: absolute;
    left: 28px;
    top: 222px;
    list-style: none;
    font-size: 13px;
    font-weight: 500;
    line-height: 19px;
  }
  .contact-list .label {
    display: inline-block;
    width: 30px;
    font-weight: 800;
  }
</style>
</head>
<body>
  <main class="sheet">
    <section class="card card-back" aria-label="Card back">
      <div class="artwork" role="img" aria-label="Yellow line drawing of a modern building over a faint architectural plan pattern"></div>
      <div class="back-brand">
        <span class="brand-name">Pixel Forum</span>
        <span class="brand-tag">ARCHITECTURE</span>
      </div>
    </section>

    <section class="card card-front" aria-label="Card front">
      <div class="front-brand">
        <span class="brand-name">Pixel Forum</span>
        <span class="brand-tag">ARCHITECTURE</span>
      </div>
      <p class="role-line">FOUNDER / <span class="person">SAM AVERY</span></p>
      <div class="divider"></div>
      <ul class="contact-list">
        <li><span class="label">P :</span>+00 000 000 000</li>
        <li><span class="label">E :</span>studio@pixelforum.example</li>
        <li><span class="label">W:</span>www.pixelforum.example</li>
      </ul>
    </section>
  </main>
</body>
</html>
```